VELMAR, an e-commerce website with a twist, providing consumer-to-consumer and business-to-consumer sa

I have only uploaded 10 wire-frame pages of the website. These pages have been chosen for the different lay-outs and should give an idea of what will be needed. There are many more that I won’t upload yet, I aim to choose a winner first then there will be a high possibility that the winner will get the chance to do the design work for these later.
The design I have in Calmpath is to keep it clean and easy with no/minimal fancy fonts and hieroglyphics. The logo is white with an orange highlight on a solid background of black, please note that the logo is white on a black background and is not a black box with white lettering, trust that makes sense. I like the idea of the top part of the website being black all the way across. I don’t see the need for more than 3 colours in the actual base website (the pictures and adverts added by users will add other colours). Although orange is the highlight colour in the logo I am open to suggestions on this, so long as the highlight colour features throughout the site.

Website width is 1220px, all pages in the PDF are 1220px

Logo font is Rezlong

The company is going to be like tradu, but much more focused on raising money for charity and humanitarian relief.

Target Market(s)

the modern era of smartphones and the sharing community

Industry/Entity Type

Business

Number of Pages Required

5+ page

Font styles to use
Sans Serif
Other font styles liked:
• rezlong

Colors
faa54b
f78f20
ffffff
000000
fbfbfb
f5f5f5

Requirements
Nice to have
• Although orange is the highlight colour in the logo I am open to suggestions on this, so long as the highlight colour features throughout the site.

```html
<!DOCTYPE html>
<html lang="en">
<head>
<meta charset="utf-8">
<title>VELMAR – Home</title>
<link href="https://fonts.googleapis.com/css2?family=Open+Sans:ital,wght@0,400;0,600;0,700;1,400&family=Montserrat:wght@400;600;700&display=swap" rel="stylesheet">
<style>
:root{
  --orange:#f78f20;
  --orange-soft:#faa54b;
  --ink:#000000;
  --dark:#2b2b2b;
  --panel:#262626;
  --white:#ffffff;
  --off:#fbfbfb;
  --light:#f5f5f5;
  --line:#e2e2e2;
  --muted:#8a8a8a;
  --blue:#2a7fc0;
  --text:#333333;
}
*{box-sizing:border-box;margin:0;padding:0}
html,body{width:690px;height:1200px;overflow:hidden;background:var(--white)}
body{position:relative;font-family:'Open Sans',Arial,sans-serif;color:var(--text)}
.abs{position:absolute}

/* top bar */
.topbar{left:0;top:0;width:690px;height:18px;background:var(--dark)}
.toplinks{right:148px;top:0;height:18px;display:flex;align-items:center;gap:7px;font-size:5.6px;color:#bdbdbd}
.toplinks .sep{color:#777}
.topicons{left:558px;top:0;display:flex;height:18px}
.topicons span{width:19px;height:18px;border-left:1px solid #444;display:flex;align-items:center;justify-content:center}
.topicons i{display:block;width:7px;height:7px;background:#8a8a8a;border-radius:1px}

/* header */
.logo{left:68px;top:33px;font-size:27px;font-weight:700;color:var(--ink);letter-spacing:-1px;line-height:1}
.search{left:166px;top:42px;width:266px;height:17px;display:flex}
.search-field{flex:1;border:1px solid #d8d8d8;border-right:none;border-radius:9px 0 0 9px;font-size:5.6px;font-style:italic;color:#aaa;padding:0 9px;display:flex;align-items:center;justify-content:space-between}
.search-btn{width:92px;background:var(--orange);color:var(--white);border-radius:0 9px 9px 0;font-size:5.8px;display:flex;align-items:center;justify-content:center;gap:3px}
.nav-link{top:46px;font-size:5.6px;font-weight:600;color:#444;display:flex;align-items:center;gap:4px;letter-spacing:.2px}
.cart{left:593px;top:41px;width:19px;height:19px;border-radius:50%;background:var(--orange);display:flex;align-items:center;justify-content:center}
.cart-count{left:605px;top:37px;width:10px;height:10px;border-radius:50%;background:var(--white);border:1px solid var(--orange);font-size:4.5px;font-weight:700;display:flex;align-items:center;justify-content:center;color:#333}

/* feature row */
.tile{left:10px;width:192px;height:101px;display:flex;flex-direction:column;align-items:center;justify-content:center;color:var(--white);font-size:8px;font-weight:600;gap:6px}
.tile-one{top:83px;background:linear-gradient(135deg,#6a6a6a,#2e2e2e 70%,#4a4a4a)}
.tile-two{top:189px;background:linear-gradient(135deg,#3b3b3b,#7a7a7a 55%,#2a2a2a)}
.play{width:24px;height:24px;border:1.5px solid var(--white);border-radius:50%;display:flex;align-items:center;justify-content:center}

.finder{left:212px;top:83px;width:266px;height:207px;background:var(--light);border:1px solid #e6e6e6}
.finder-head{height:32px;background:var(--dark);color:var(--white);font-size:11px;display:flex;align-items:center;justify-content:center}
.finder-body{padding:8px 9px}
.f-label{font-size:7.3px;color:#888;margin:6px 0 3px}
.f-input{height:17px;background:var(--white);border:1px solid #e4e4e4;display:flex}
.f-input .grow{flex:1}
.f-input .help{width:17px;border-left:1px solid #e4e4e4;font-size:5px;color:#aaa;display:flex;align-items:center;justify-content:center}
.f-input .half{flex:1;font-size:5.5px;color:#aaa;padding-left:8px;display:flex;align-items:center;border-right:1px solid #e4e4e4}
.f-btn{margin-top:18px;height:17px;background:var(--orange);color:var(--white);font-size:7.5px;display:flex;align-items:center;justify-content:center}

.recent{left:488px;top:83px;width:193px;height:207px;background:var(--panel);padding:8px 9px}
.recent-item{display:flex;gap:10px;height:63px;padding-top:1px;border-bottom:1px solid #444;margin-bottom:4px}
.recent-item:last-child{border-bottom:none}
.thumb{width:56px;height:56px;background:var(--white);flex:none;display:flex;align-items:center;justify-content:center}
.thumb i{display:block;width:40px;height:36px}
.recent-title{font-size:7.5px;color:var(--white);margin-top:4px}
.recent-title.link{text-decoration:underline}
.recent-desc{font-size:5.6px;color:#cfcfcf;line-height:1.5;margin-top:3px}
.recent-price{font-size:6.4px;color:var(--orange);margin-top:6px;font-weight:600}

/* promos */
.promo{left:74px;width:543px;height:92px}
.promo-camera{top:318px;background:linear-gradient(90deg,#2a2a2a,#5a5550 30%,#6a4a33 60%,#7a5438)}
.promo-watch{top:802px;background:linear-gradient(90deg,#5a3a22,#8a6a4a 30%,#a06a3a 60%,#6a4028)}
.promo-copy{left:329px;font-family:'Montserrat',Arial,sans-serif;color:var(--white)}
.promo-kicker{font-size:5.4px;font-weight:600;letter-spacing:1px}
.promo-title{font-size:16px;font-weight:400;margin-top:3px}
.promo-title b{font-weight:700}
.promo-btn{display:inline-block;margin-top:6px;background:#111;font-size:5px;font-weight:700;letter-spacing:.6px;padding:5px 11px}

/* feedback */
.feedback{left:0;top:438px;width:690px;height:336px;background:var(--blue)}
.feedback-title{left:0;top:23px;width:690px;text-align:center;font-size:16px;color:var(--white)}
.card{top:59px;width:174px;height:206px;background:var(--white);text-align:center}
.quote{margin-top:14px;height:20px}
.card-text{font-size:8px;font-style:italic;color:#888;line-height:1.45;padding:0 19px;margin-top:8px;height:88px}
.stars{font-size:7px;color:var(--orange);letter-spacing:1px;margin-top:4px}
.name{font-size:8.6px;font-weight:600;color:#333;margin-top:4px;letter-spacing:.3px}
.place{font-size:5.8px;color:#888}
.avatar{top:236px;width:46px;height:46px;border-radius:50%;border:2px solid var(--white)}
.feedback-link{left:0;top:302px;width:690px;text-align:center;font-size:7px;color:var(--white);text-decoration:underline}

/* charities & ads */
.sec-title{top:926px;font-size:8px;font-weight:600;color:#333;padding-bottom:7px;border-bottom:1px solid var(--line)}
.charity-grid{left:74px;top:956px;width:257px;display:grid;grid-template-columns:repeat(3,83px);grid-auto-rows:48px;gap:3px 4px}
.charity{background:var(--light);display:flex;align-items:center;justify-content:center;font-size:7.5px;font-weight:700;color:#3a3a3a;text-align:center;line-height:1.1}
.pager{left:74px;top:1109px;width:257px;height:17px;border:1px solid #ececec;background:var(--off)}
.dots{left:104px;top:8px;display:flex;gap:3px}
.dots i{display:block;width:9px;height:1.5px;background:#d8d8d8}
.dots i.on{background:var(--orange)}
.ad{left:358px;width:258px;height:83px}
.ad-one{top:956px;background:linear-gradient(90deg,#8a8a86,#b8b6b0 50%,#d9d7d2)}
.ad-two{top:1043px;background:linear-gradient(90deg,#e8e7e3,#d4d2cc 55%,#6c6e72)}
.ad-save{left:32px;top:16px;color:var(--white);display:flex;align-items:center;gap:3px;font-family:'Montserrat',Arial,sans-serif}
.ad-save small{font-size:10px;line-height:1;font-weight:400}
.ad-save b{font-size:26px;font-weight:700}
.ad-bed{left:24px;top:29px;font-family:'Montserrat',Arial,sans-serif;color:#222}
.ad-bed .k{font-size:5px;letter-spacing:.3px}
.ad-bed .g{font-size:17px;font-weight:700;color:#7ab0dc;line-height:1}
.ad-bed .s{font-size:7.5px;font-weight:700;letter-spacing:.4px}

/* footer */
.footer{left:0;top:1154px;width:690px;height:46px;background:var(--dark)}
.foot-links{left:74px;top:19px;font-size:6px;color:#b5b5b5;display:flex;gap:4px}
.foot-links .on{color:var(--orange)}
.foot-right{left:410px;top:19px;font-size:6px;color:#b5b5b5}
.social{left:530px;top:17px;display:flex;gap:3px}
.social i{display:block;width:10px;height:10px;background:#9a9a9a;border-radius:2px}
</style>
</head>
<body>

<!-- top bar -->
<div class="abs topbar"></div>
<div class="abs toplinks"><span>List Item</span><span class="sep">/</span><span>Terms &amp; Conditions</span><span class="sep">/</span><span>Contact Us</span></div>
<div class="abs topicons"><span><i></i></span><span><i></i></span><span><i></i></span></div>

<!-- header -->
<div class="abs logo">velmar</div>
<div class="abs search">
  <div class="search-field">Search here ...
    <svg width="7" height="7" viewBox="0 0 10 10"><circle cx="4" cy="4" r="3" fill="none" stroke="#f78f20" stroke-width="1.5"/><line x1="6.3" y1="6.3" x2="9" y2="9" stroke="#f78f20" stroke-width="1.5"/></svg>
  </div>
  <div class="search-btn">+ My Recent Searches</div>
</div>
<div class="abs nav-link" style="left:466px">
  <svg width="7" height="7" viewBox="0 0 10 10"><path d="M1 5h5M4 2.5 6.5 5 4 7.5M7 1h2v8H7" fill="none" stroke="#555" stroke-width="1.2"/></svg>SIGN IN</div>
<div class="abs nav-link" style="left:518px">
  <svg width="7" height="7" viewBox="0 0 10 10"><path d="M5 9 1 5a2.2 2.2 0 0 1 4-3 2.2 2.2 0 0 1 4 3z" fill="#777"/></svg>WISHLIST</div>
<div class="abs cart"><svg width="9" height="9" viewBox="0 0 10 10"><path d="M1 2h1.5l1.2 5h4.5L9 3.5H3" fill="none" stroke="#fff" stroke-width="1.2"/><circle cx="4.3" cy="8.6" r=".8" fill="#fff"/><circle cx="7.6" cy="8.6" r=".8" fill="#fff"/></svg></div>
<div class="abs cart-count">03</div>

<!-- feature row -->
<div class="abs tile tile-one" role="img" aria-label="Crowd with raised hands, black and white video still">
  <div class="play"><svg width="8" height="9" viewBox="0 0 8 9"><path d="M1 0.5v8l6.5-4z" fill="#fff"/></svg></div>
  <div>Discover about velmar</div>
</div>
<div class="abs tile tile-two" role="img" aria-label="Child in a woollen hat, black and white video still">
  <div class="play"><svg width="8" height="9" viewBox="0 0 8 9"><path d="M1 0.5v8l6.5-4z" fill="#fff"/></svg></div>
  <div>velmar does for charity</div>
</div>

<div class="abs finder">
  <div class="finder-head">Search your Items</div>
  <div class="finder-body">
    <div class="f-label">Your Item</div>
    <div class="f-input"><div class="grow"></div><div class="help">?</div></div>
    <div class="f-label">Enter your Location</div>
    <div class="f-input"><div class="grow"></div><div class="help">?</div></div>
    <div class="f-label">Price</div>
    <div class="f-input"><div class="half">From ( £ )</div><div class="half">To ( £ )</div><div class="help">?</div></div>
    <div class="f-btn">Search</div>
  </div>
</div>

<div class="abs recent">
  <div class="recent-item">
    <div class="thumb"><i role="img" aria-label="Tablet product photo" style="background:linear-gradient(135deg,#7fd0e8,#e88fc8 50%,#f0d070)"></i></div>
    <div><div class="recent-title link">Lorem ipsum dolor sit</div><div class="recent-desc">Sed ut perspiciatis unde omnis iste natus error sit ...</div><div class="recent-price">£300.00</div></div>
  </div>
  <div class="recent-item">
    <div class="thumb"><i role="img" aria-label="Yellow and black headset product photo" style="background:linear-gradient(90deg,#222,#e8d21a 40%,#f0df30 60%,#222)"></i></div>
    <div><div class="recent-title">Unde omnis iste</div><div class="recent-desc">Sed ut perspiciatis unde omnis iste natus error sit ...</div><div class="recent-price">£120.00</div></div>
  </div>
  <div class="recent-item">
    <div class="thumb"><i role="img" aria-label="Black and green game controller product photo" style="background:radial-gradient(circle,#1a1a1a 45%,#3bcf3b 75%,#fff 76%)"></i></div>
    <div><div class="recent-title">Consectetur adipiscing</div><div class="recent-desc">Sed ut perspiciatis unde omnis iste natus error sit ...</div><div class="recent-price">£96.00</div></div>
  </div>
</div>

<!-- promo one -->
<div class="abs promo promo-camera" role="img" aria-label="Vintage camera lens on a wooden table">
  <div class="abs promo-copy" style="top:27px">
    <div class="promo-kicker">HOT PROMOTION</div>
    <div class="promo-title">Save Up to <b>40%</b> Off</div>
    <div class="promo-btn">BUY NOW</div>
  </div>
</div>

<!-- feedback -->
<section class="abs feedback">
  <div class="abs feedback-title">User Feedback</div>

  <svg class="abs" style="left:46px;top:159px" width="10" height="9" viewBox="0 0 10 9"><path d="M9 8C8 4 6 3 3.5 3.5V1L0 4.5 3.5 8V5.5C6 5 8 6 9 8z" fill="#6fa8d6"/></svg>
  <svg class="abs" style="left:636px;top:159px" width="10" height="9" viewBox="0 0 10 9"><path d="M1 8C2 4 4 3 6.5 3.5V1L10 4.5 6.5 8V5.5C4 5 2 6 1 8z" fill="#fff"/></svg>

  <div class="abs card" style="left:74px">
    <svg class="quote" width="22" height="18" viewBox="0 0 22 18"><path d="M1 8c0-4 2-6.5 6-7v2.5c-2 .5-3 2-3 3.5h3v9H1zM12 8c0-4 2-6.5 6-7v2.5c-2 .5-3 2-3 3.5h3v9h-6z" fill="none" stroke="#bbb" stroke-width="1.2"/></svg>
    <p class="card-text">Lorem Ipsum has been the industry's standard dummy text ever since the 1500s, when an unknown printer took a galley of type and scrambled it to make a type specimen book.</p>
    <div class="stars">★★★★☆</div>
    <div class="name">Mara Ellis</div>
    <div class="place">New York, NY</div>
  </div>
  <div class="abs card" style="left:258px">
    <svg class="quote" width="22" height="18" viewBox="0 0 22 18"><path d="M1 8c0-4 2-6.5 6-7v2.5c-2 .5-3 2-3 3.5h3v9H1zM12 8c0-4 2-6.5 6-7v2.5c-2 .5-3 2-3 3.5h3v9h-6z" fill="none" stroke="#f78f20" stroke-width="1.2"/></svg>
    <p class="card-text">Lorem Ipsum has been the industry's standard dummy text ever since the 1500s, when an unknown printer took a galley of type and scrambled it to make a type specimen book.</p>
    <div class="stars">★★★★☆</div>
    <div class="name">Owen Darrow</div>
    <div class="place">Maplewood, NJ</div>
  </div>
  <div class="abs card" style="left:442px">
    <svg class="quote" width="22" height="18" viewBox="0 0 22 18"><path d="M1 8c0-4 2-6.5 6-7v2.5c-2 .5-3 2-3 3.5h3v9H1zM12 8c0-4 2-6.5 6-7v2.5c-2 .5-3 2-3 3.5h3v9h-6z" fill="none" stroke="#bbb" stroke-width="1.2"/></svg>
    <p class="card-text">Lorem Ipsum has been the industry's standard dummy text ever since the 1500s, when an unknown printer took a galley of type and scrambled it to make a type specimen book.</p>
    <div class="stars">★★★★☆</div>
    <div class="name">Priya Nolan</div>
    <div class="place">Chicago, IL</div>
  </div>

  <div class="abs avatar" style="left:138px;background:radial-gradient(circle at 50% 40%,#c9a58a,#5a4030)" role="img" aria-label="Portrait photo of reviewer"></div>
  <div class="abs avatar" style="left:322px;background:radial-gradient(circle at 50% 40%,#c8a088,#2e2e36)" role="img" aria-label="Portrait photo of reviewer"></div>
  <div class="abs avatar" style="left:506px;background:radial-gradient(circle at 50% 40%,#e2c0a0,#b08a5a)" role="img" aria-label="Portrait photo of reviewer"></div>

  <div class="abs feedback-link">→ Leave a feedback for a chance to win a prize</div>
</section>

<!-- promo two -->
<div class="abs promo promo-watch" role="img" aria-label="Pocket watch with autumn leaves">
  <div class="abs promo-copy" style="top:28px">
    <div class="promo-kicker">HOT PROMOTION</div>
    <div class="promo-title">Save Up to <b>40%</b> Off</div>
    <div class="promo-btn">BUY NOW</div>
  </div>
</div>

<!-- charities -->
<div class="abs sec-title" style="left:74px;width:257px">Charities Supported</div>
<div class="charity-grid abs">
  <div class="charity">Kindwell</div>
  <div class="charity">Givecrest</div>
  <div class="charity">Unity Fund</div>
  <div class="charity">Calmpath</div>
  <div class="charity">Harbora</div>
  <div class="charity">Little Lantern</div>
  <div class="charity">Oak Ladle</div>
  <div class="charity">Skyarc</div>
  <div class="charity">tradu for Charity</div>
</div>
<div class="abs pager">
  <svg class="abs" style="left:6px;top:4px" width="9" height="8" viewBox="0 0 10 9"><path d="M9 8C8 4 6 3 3.5 3.5V1L0 4.5 3.5 8V5.5C6 5 8 6 9 8z" fill="#ccc"/></svg>
  <div class="abs dots"><i></i><i class="on"></i><i></i><i></i></div>
  <svg class="abs" style="left:242px;top:4px" width="9" height="8" viewBox="0 0 10 9"><path d="M1 8C2 4 4 3 6.5 3.5V1L10 4.5 6.5 8V5.5C4 5 2 6 1 8z" fill="#2a7fc0"/></svg>
</div>

<!-- advertisement -->
<div class="abs sec-title" style="left:358px;width:258px">Advertisement</div>
<div class="abs ad ad-one" role="img" aria-label="Grey room with white side table and cushions">
  <div class="abs ad-save"><small>SAVE<br>UPTO</small><b>70%</b></div>
</div>
<div class="abs ad ad-two" role="img" aria-label="Bedroom stool with pastel cushion and lamp">
  <div class="abs ad-bed"><div class="k">BEDROOM FURNITURE</div><div class="g">GOOD</div><div class="s">NIGHT'S SLEED</div></div>
</div>

<!-- footer -->
<footer class="abs footer">
  <div class="abs foot-links"><span>About velmar</span>/<span class="on">Safety hub</span>/<span>Resolution hub</span>/<span>Vendor hub</span>/<span>Partner hub</span>/<span>Charity hub</span></div>
  <div class="abs foot-right">Advertisement on velmar / Sitemap</div>
  <div class="abs social"><i></i><i></i><i></i><i></i><i></i><i></i><i></i></div>
</footer>

</body>
</html>
```